Lakeshore Vision Associates, P.C.
Diseases and Surgeries of the Retina, Macula and Vitreous
Lakeshore Vision Associates, P.C. - Medical
Creative Brief
Professional
Peter R. Haldane, MD
Birchwood Medical Tower 4215 N. Lindon Suite 812 Wexmore, IL 60952
peter@lakeshorevsa.com
www.lakeshorevsa.com
Appointment Date: MM/DD/YYYY at ____________am ___________pm Please telephone in advance if you will be unable to keep the appointment

```html
<!DOCTYPE html>
<html lang="en">
<head>
<meta charset="utf-8">
<title>Lakeshore Vision Associates, P.C. – Stationery</title>
<link href="https://fonts.googleapis.com/css2?family=Lato:wght@400;700&display=swap" rel="stylesheet">
<style>
  :root{
    --bg:#e8e3da;
    --paper:#ffffff;
    --paper-shade:#f3f1ee;
    --ink:#5a5a5a;
    --ink-soft:#8a8a8a;
    --orange-deep:#d4521a;
    --orange:#e8702a;
    --orange-light:#f4a04a;
    --shadow:rgba(40,25,10,.28);
  }
  *{box-sizing:border-box;margin:0;padding:0}
  html,body{width:1200px;height:715px;overflow:hidden}
  body{background:var(--bg);font-family:"Lato",Arial,sans-serif;color:var(--ink);position:relative}

  .brand{display:flex;align-items:center;gap:7px}
  .brand-square{width:18px;height:18px;background:var(--ink);flex:none}
  .brand-name{font-size:9px;letter-spacing:.14em;text-transform:uppercase;color:var(--ink);font-weight:400;line-height:1.25}

  .card{position:absolute;left:72px;width:216px;height:128px;border-radius:8px;background:var(--paper);box-shadow:2px 3px 8px var(--shadow);overflow:hidden}
  .card--front{top:79px;padding:14px}
  .card--appointment{top:222px;padding:14px}
  .card--orange-a{top:364px;background:linear-gradient(90deg,var(--orange-deep),var(--orange) 60%,var(--orange-light))}
  .card--orange-b{top:500px;background:linear-gradient(90deg,var(--orange-deep),var(--orange) 60%,var(--orange-light))}
  .card-details{margin-top:14px;margin-left:25px;font-size:6px;line-height:1.55;color:var(--ink)}
  .card-details .doctor{font-weight:700}
  .appointment-text{position:relative;font-size:6px;line-height:1.7;color:var(--ink-soft);width:150px}
  .card-shade{position:absolute;left:0;top:0;width:120px;height:100%;background:linear-gradient(90deg,rgba(0,0,0,.04),rgba(0,0,0,0))}
  .card-url{position:absolute;right:14px;bottom:12px;font-size:6px;color:rgba(255,255,255,.95);letter-spacing:.04em}

  .sheet{position:absolute;width:372px;height:540px;background:var(--paper);box-shadow:2px 4px 10px var(--shadow)}
  .sheet--back{left:340px;top:86px;transform:rotate(-3deg);background:var(--paper-shade)}
  .sheet--front{left:322px;top:72px;padding:22px 26px;overflow:hidden}
  .sheet-address{margin-top:10px;margin-left:25px;font-size:6px;line-height:1.6;color:var(--ink)}
  .sheet-contact{position:absolute;left:0;width:100%;text-align:center;top:222px;font-size:6px;color:var(--ink-soft);letter-spacing:.04em}
  .sheet-watermark{position:absolute;left:50px;top:255px;width:270px;height:270px;border-radius:50%;
    background:radial-gradient(circle,rgba(245,200,160,.32) 0,rgba(245,215,190,.22) 45%,rgba(235,235,235,.3) 60%,rgba(255,255,255,0) 71%)}

  .envelope{position:absolute;left:750px;width:342px;height:150px;background:var(--paper);box-shadow:2px 3px 8px var(--shadow);overflow:hidden}
  .envelope svg{position:absolute;left:0;top:0}
  .envelope--orange{top:318px}
  .envelope--white{top:356px}
  .envelope--front{top:410px;height:152px;padding:16px}
  .envelope-address{margin-top:8px;margin-left:25px;font-size:6px;line-height:1.6;color:var(--ink)}
</style>
</head>
<body>

  <section class="card card--front">
    <div class="brand"><span class="brand-square"></span><span class="brand-name">Lakeshore Vision<br>Associates</span></div>
    <div class="card-details">
      <div class="doctor">Peter R. Haldane, MD</div>
      <div>Birchwood Medical Tower</div>
      <div>4215 N. Lindon Suite 812</div>
      <div>Wexmore, IL 60952</div>
      <div>T 847.555.0142</div>
      <div>F 847.555.0143</div>
      <div>peter@lakeshorevsa.com</div>
    </div>
  </section>

  <section class="card card--appointment">
    <span class="card-shade"></span>
    <p class="appointment-text">Appointment Date: MM/DD/YYYY<br>at ________ am ________ pm<br>Please telephone in advance if you will be unable to keep the appointment</p>
  </section>

  <section class="card card--orange-a">
    <span class="card-shade"></span>
  </section>

  <section class="card card--orange-b">
    <span class="card-shade"></span>
    <span class="card-url">www.lakeshorevsa.com</span>
  </section>

  <div class="sheet sheet--back"></div>
  <section class="sheet sheet--front">
    <div class="brand"><span class="brand-square"></span><span class="brand-name">Lakeshore Vision<br>Associates</span></div>
    <div class="sheet-address">
      <div>Birchwood Medical Tower</div>
      <div>4215 N. Lindon Suite 812 Wexmore, IL 60952</div>
      <div>T 847.555.0142 &nbsp; F 847.555.0143</div>
    </div>
    <div class="sheet-contact">peter@lakeshorevsa.com &nbsp;&nbsp; www.lakeshorevsa.com</div>
    <div class="sheet-watermark" role="img" aria-label="Faint retina photograph watermark"></div>
  </section>

  <section class="envelope envelope--orange">
    <svg width="342" height="150" viewBox="0 0 342 150" aria-hidden="true">
      <defs>
        <linearGradient id="flapOrange" x1="0" x2="1">
          <stop offset="0" stop-color="#d4521a"/><stop offset=".6" stop-color="#e8702a"/><stop offset="1" stop-color="#f4a04a"/>
        </linearGradient>
      </defs>
      <path d="M0 0 H342 L182 60 Q171 64 160 60 Z" fill="url(#flapOrange)"/>
    </svg>
  </section>

  <section class="envelope envelope--white">
    <svg width="342" height="150" viewBox="0 0 342 150" aria-hidden="true">
      <path d="M0 0 H342 L182 74 Q171 78 160 74 Z" fill="#fafafa" stroke="#dcdcdc" stroke-width="1"/>
    </svg>
  </section>

  <section class="envelope envelope--front">
    <div class="brand"><span class="brand-square"></span><span class="brand-name">Lakeshore Vision<br>Associates</span></div>
    <div class="envelope-address">
      <div>Birchwood Medical Tower</div>
      <div>4215 N. Lindon Suite 812</div>
      <div>Wexmore, IL 60952</div>
    </div>
  </section>

</body>
</html>
```